Chiropractic healthcare group business card

We are a Portland Oregon based chiropractic healthcare group. Looking for a new business card design. Something cutting edge, that shows off our new logo and tag line.Use either of the attached logos.Our tag line = "Who would you be without pain?"I'm open to about anything, impress me!!
Target Market(s)
Chiropractic patients - Auto injury, back pain, sports injuries, neck , shoulder, hip, knee, ankle pain.
Industry/Entity Type
Chiropractic
Contact Information for Business Card
Dr. Bram Holtvick, D.C.
Clinic name - Fernway Chiropractic
2 clinics
location #1
20418 NW Marwick Road
Suite B
North Plains, OR 97133
Location #2
13529 SE Calloway Street
Portland OR 97236
Main phone line 971.555.0143
website : www.FernwayClinics.example
Tag line "Who would you be without pain?"
Colors
Designer to choose colors to be used in the design.
Requirements
Must have
- Use the logo colors -- Want the orange color to be a TRUE orange.
- Both clinic address
- phone number
- website
- personal email - b.holtvick@ReliefBeginsHere.example
- tag line - "Who would you be without pain?"

```html
<!DOCTYPE html>
<html lang="en">
<head>
<meta charset="UTF-8">
<title>Fernway Chiropractic – Business Card</title>
<link rel="stylesheet" href="https://fonts.googleapis.com/css2?family=Montserrat:wght@400;500;700&display=swap">
<style>
  :root {
    --page-bg: #e9ecef;
    --card-bg: #ffffff;
    --brand-blue: #1f7fc4;
    --brand-navy: #1c3f6e;
    --brand-orange: #ff7f00;
    --logo-grey: #5a6470;
    --text-dark: #2b2f36;
  }
  * { box-sizing: border-box; margin: 0; padding: 0; }
  html, body {
    width: 1200px; height: 862px; overflow: hidden;
    background: var(--page-bg);
    font-family: "Montserrat", sans-serif;
  }
  .business-card {
    position: absolute; left: 160px; top: 180px;
    width: 880px; height: 503px;
    background: var(--card-bg);
    border-radius: 14px;
    box-shadow: 0 10px 30px rgba(0,0,0,0.15);
    overflow: hidden;
  }
  .card-stripes { position: absolute; left: 0; top: 0; }
  .brand-mark {
    position: absolute; left: 56px; top: 46px;
    display: flex; align-items: center; gap: 14px;
  }
  .brand-square { width: 34px; height: 34px; background: var(--brand-orange); }
  .brand-name {
    font-weight: 500; font-size: 17px; letter-spacing: 5px;
    color: var(--logo-grey); text-transform: uppercase; line-height: 1.35;
  }
  .card-details { position: absolute; left: 330px; top: 96px; right: 40px; }
  .doctor-name {
    font-weight: 700; font-size: 27px; color: var(--brand-blue);
    text-transform: uppercase; letter-spacing: 0.5px;
  }
  .tagline {
    margin-top: 8px; font-weight: 500; font-size: 13px;
    color: var(--text-dark); text-transform: uppercase; letter-spacing: 1px;
  }
  .contact-list { list-style: none; margin-top: 52px; }
  .contact-item {
    display: flex; align-items: center; gap: 16px;
    font-size: 14px; color: var(--text-dark); height: 40px;
  }
  .contact-icon { width: 18px; height: 18px; flex: none; fill: var(--brand-blue); }
</style>
</head>
<body>
  <section class="business-card">
    <svg class="card-stripes" width="880" height="503" viewBox="0 0 880 503" aria-hidden="true">
      <polygon points="0,170 30,170 230,503 0,503" fill="var(--brand-blue)"/>
      <line x1="46" y1="170" x2="246" y2="503" stroke="var(--brand-navy)" stroke-width="4"/>
      <polygon points="62,170 84,170 284,503 262,503" fill="var(--brand-orange)"/>
      <line x1="100" y1="200" x2="282" y2="503" stroke="var(--brand-navy)" stroke-width="2"/>
      <line x1="0" y1="420" x2="50" y2="503" stroke="var(--brand-orange)" stroke-width="5"/>
    </svg>

    <div class="brand-mark">
      <span class="brand-square"></span>
      <span class="brand-name">Fernway<br>Chiropractic</span>
    </div>

    <div class="card-details">
      <h1 class="doctor-name">Dr. Bram Holtvick, D.C.</h1>
      <p class="tagline">Who would you be without pain?</p>

      <ul class="contact-list">
        <li class="contact-item">
          <svg class="contact-icon" viewBox="0 0 24 24"><path d="M12 2a7 7 0 0 0-7 7c0 5 7 13 7 13s7-8 7-13a7 7 0 0 0-7-7zm0 9.5A2.5 2.5 0 1 1 12 6.5a2.5 2.5 0 0 1 0 5z"/></svg>
          20418 NW Marwick Road, Suite B, North Plains, OR 97133
        </li>
        <li class="contact-item">
          <svg class="contact-icon" viewBox="0 0 24 24"><path d="M12 2a7 7 0 0 0-7 7c0 5 7 13 7 13s7-8 7-13a7 7 0 0 0-7-7zm0 9.5A2.5 2.5 0 1 1 12 6.5a2.5 2.5 0 0 1 0 5z"/></svg>
          13529 SE Calloway Street, Portland, OR 97236
        </li>
        <li class="contact-item">
          <svg class="contact-icon" viewBox="0 0 24 24"><path d="M12 2a10 10 0 1 0 0 20 10 10 0 0 0 0-20zm6.9 9h-3a15 15 0 0 0-1.3-5.6A8 8 0 0 1 18.9 11zM12 4c.9 1.2 1.8 3.6 2 7h-4c.2-3.4 1.1-5.8 2-7zM9.4 5.4A15 15 0 0 0 8.1 11h-3a8 8 0 0 1 4.3-5.6zM5.1 13h3a15 15 0 0 0 1.3 5.6A8 8 0 0 1 5.1 13zM12 20c-.9-1.2-1.8-3.6-2-7h4c-.2 3.4-1.1 5.8-2 7zm2.6-1.4a15 15 0 0 0 1.3-5.6h3a8 8 0 0 1-4.3 5.6z"/></svg>
          www.FernwayClinics.example
        </li>
        <li class="contact-item">
          <svg class="contact-icon" viewBox="0 0 24 24"><path d="M3 5h18v14H3zm2 2v.5l7 5 7-5V7zm0 3v7h14v-7l-7 5z"/></svg>
          b.holtvick@ReliefBeginsHere.example
        </li>
        <li class="contact-item">
          <svg class="contact-icon" viewBox="0 0 24 24"><path d="M6.6 10.8a15 15 0 0 0 6.6 6.6l2.2-2.2a1 1 0 0 1 1-.25 11.4 11.4 0 0 0 3.6.57 1 1 0 0 1 1 1V20a1 1 0 0 1-1 1A17 17 0 0 1 3 4a1 1 0 0 1 1-1h3.5a1 1 0 0 1 1 1c0 1.25.2 2.45.57 3.57a1 1 0 0 1-.25 1z"/></svg>
          971.555.0143
        </li>
      </ul>
    </div>
  </section>
</body>
</html>
```